Dental Lab flyer

I would like eye catching dental lab flyer. Promoting Q.vex , Birelo Zirconia, and 7K Duvo Prisma Zirconia.
Price Q.vex $85
Birelo $44
7K $56

```html
<!DOCTYPE html>
<html lang="en">
<head>
<meta charset="utf-8">
<title>Crestline Dental – Lab Flyer</title>
<link href="https://fonts.googleapis.com/css2?family=Poppins:wght@300;400;500;600;700;800&family=Anton&display=swap" rel="stylesheet">
<style>
:root{
  --ink:#231f20;
  --blue:#4bb8e0;
  --grey:#e9e9ea;
  --white:#ffffff;
  --text:#3a3a3a;
  --crimson:#c2185b;
  --purple:#8e2a9e;
  --red:#e21f26;
  --page:#f2f2f2;
}
*{margin:0;padding:0;box-sizing:border-box}
html,body{width:1200px;height:2366px;overflow:hidden;background:var(--page)}
body{position:relative;font-family:'Poppins',sans-serif}
.flyer{
  position:absolute;left:50px;top:405px;width:725px;height:1025px;
  transform:scale(1.5172);transform-origin:0 0;
  background:var(--white);overflow:hidden;
  box-shadow:0 2px 6px rgba(0,0,0,.15);
}
.hero{position:absolute;left:0;top:0;width:725px;height:370px;background:var(--ink)}
.offer-band{position:absolute;left:0;top:370px;width:725px;height:252px;background:var(--grey)}
.footer-band{position:absolute;left:0;top:960px;width:725px;height:65px;background:var(--grey)}

.brand{position:absolute;left:50px;top:38px;width:180px;text-align:center;color:var(--white)}
.brand-mark{width:44px;height:44px;border:3px solid var(--white);border-radius:50%;margin:0 auto 10px}
.brand-name{font-size:17px;font-weight:400;letter-spacing:2px}

.dots{position:absolute;left:50px;top:157px;display:flex;gap:4px}
.dots span{width:9px;height:9px;border-radius:50%;background:var(--blue)}
.dots span:nth-child(2),.dots span:nth-child(3){opacity:.7}

.headline{position:absolute;left:48px;top:170px;color:var(--white);line-height:.95}
.headline .light{display:block;font-size:50px;font-weight:400}
.headline .strong{display:block;font-size:72px;font-weight:800;color:var(--blue);line-height:.95}

.ribbon{position:absolute;left:50px;top:357px;width:232px;height:66px;background:var(--blue);
  display:flex;align-items:center;padding-left:14px;border-radius:2px}
.ribbon::before,.ribbon::after{content:"";position:absolute;top:-5px;width:20px;height:6px;background:#2e8db0}
.ribbon::before{left:-15px;transform:skewX(-30deg)}
.ribbon::after{right:-15px;transform:skewX(30deg)}
.ribbon .big{font-family:'Anton',sans-serif;font-size:38px;color:var(--ink);letter-spacing:.5px}
.ribbon .small{font-size:19px;line-height:.95;color:var(--white);margin-left:10px;font-weight:400}

.hero-photo{position:absolute;left:320px;top:18px;width:330px;height:352px;
  background:linear-gradient(180deg,#c9a88a 0%,#e9e4df 45%,#f6f6f6 100%);border-radius:6px 6px 0 0}

.arch{position:absolute;top:445px;width:184px;height:177px;border:8px solid;border-bottom:none;
  border-radius:92px 92px 0 0;padding:6px 6px 0}
.arch .fill{width:100%;height:100%;border-radius:80px 80px 0 0}
.arch-1{left:48px;border-color:var(--crimson)}
.arch-1 .fill{background:linear-gradient(160deg,#b78c72,#5b6f8c)}
.arch-2{left:272px;border-color:var(--purple)}
.arch-2 .fill{background:linear-gradient(160deg,#d7a497,#f2e8e4 60%,#caa095)}
.arch-3{left:495px;border-color:var(--red)}
.arch-3 .fill{background:linear-gradient(160deg,#8fa3c7,#3b7fd0)}

.product{position:absolute;top:640px;width:185px}
.product-1{left:48px}.product-2{left:271px}.product-3{left:495px}
.product-head{display:flex;justify-content:space-between;align-items:baseline;margin-bottom:8px}
.product-name{font-size:29px;font-weight:400;color:var(--ink)}
.price{font-size:28px;font-weight:700;color:var(--blue)}
.product p{font-size:9.4px;line-height:12px;color:var(--text);text-align:justify;margin-bottom:11px}
.product-brand{position:absolute;top:882px;display:flex;align-items:center;gap:6px;
  font-size:24px;font-weight:600;color:var(--ink)}
.product-brand.b1{left:50px;color:var(--crimson)}
.product-brand.b2{left:272px;color:var(--purple);font-size:20px}
.product-brand.b3{left:498px;color:var(--red);font-size:21px}
.product-brand .sq{width:12px;height:12px;background:currentColor}

.contact{position:absolute;left:50px;top:945px;width:625px;height:56px;border-radius:28px;overflow:hidden;display:flex}
.contact .phone{width:290px;background:var(--blue);display:flex;align-items:center;justify-content:center;gap:10px;
  font-size:31px;font-weight:700;color:var(--white)}
.contact .web{flex:1;background:var(--ink);display:flex;align-items:center;justify-content:center;gap:10px;
  font-size:22px;color:var(--white);clip-path:polygon(12px 0,100% 0,100% 100%,0 100%);margin-left:-12px}
</style>
</head>
<body>
<div class="flyer">
  <div class="hero"></div>
  <div class="offer-band"></div>
  <div class="footer-band"></div>

  <div class="brand">
    <div class="brand-mark"></div>
    <div class="brand-name">CRESTLINE DENTAL</div>
  </div>

  <div class="dots"><span></span><span></span><span></span></div>
  <h1 class="headline">
    <span class="light">IMPROVE</span>
    <span class="light">YOUR</span>
    <span class="strong">SMILE</span>
  </h1>

  <div class="hero-photo" role="img" aria-label="Smiling dental technician in a white coat holding a dental model"></div>

  <div class="ribbon"><span class="big">A FREE</span><span class="small">EXAM<br>&amp; X-RAY!</span></div>

  <div class="arch arch-1"><div class="fill" role="img" aria-label="Patient in dental chair during a check-up"></div></div>
  <div class="arch arch-2"><div class="fill" role="img" aria-label="Close-up of a bright smile before and after whitening"></div></div>
  <div class="arch arch-3"><div class="fill" role="img" aria-label="Child patient being treated by a dentist"></div></div>

  <section class="product product-1">
    <div class="product-head"><h2 class="product-name">Q.VEX</h2><span class="price">$85</span></div>
    <p>QS Q.vex combines high esthetic vitality with high performance. This innovative lithium disilicate ceramic fulfills the highest esthetic demands and unites state-of-the-art technology with exceptional user friendliness. QS Q.vex is a lithium disilicate glass ceramic with optimized translucency, durability and strength for full anatomical restorations. QS Q.vex is available as a pressed and as a CAD/CAM milled technology.</p>
  </section>

  <section class="product product-2">
    <div class="product-head"><h2 class="product-name">BIRELO</h2><span class="price">$44</span></div>
    <p>Create partials, natural veneers, full contour prosthetics and large dentin-like frameworks with our line of zirconia disks. Reach the highest level of esthetic in usually less steps than our competition. The great properties of the material will get you a natural for the eye pleasing result even right after sintering.</p>
    <p>With the introduction of our translucent series: SV and UV, we have created a new standard for anterior prosthetics.</p>
  </section>

  <section class="product product-3">
    <div class="product-head"><h2 class="product-name">7K</h2><span class="price">$56</span></div>
    <p>At 7K, we apply science in collaborative ways to improve lives daily. Learn more about our company, our people, and the impact we make.At 7K, our 93,000 employees do work that matters, applying our science in ways that make a positive impact on people's lives around the globe.</p>
    <p>And that work is accomplished through close collaboration with smart,</p>
  </section>

  <div class="product-brand b1"><span>Q.vex</span></div>
  <div class="product-brand b2"><span class="sq"></span><span>Birelo Zirconia</span></div>
  <div class="product-brand b3"><span>7K Duvo Prisma</span></div>

  <div class="contact">
    <div class="phone">
      <svg width="24" height="24" viewBox="0 0 24 24" aria-hidden="true"><path fill="#231f20" d="M6.6 10.8a15.1 15.1 0 0 0 6.6 6.6l2.2-2.2c.3-.3.7-.4 1-.2 1.1.4 2.3.6 3.6.6.6 0 1 .4 1 1V20c0 .6-.4 1-1 1A17 17 0 0 1 3 4c0-.6.4-1 1-1h3.5c.6 0 1 .4 1 1 0 1.3.2 2.5.6 3.6.1.3 0 .7-.2 1z"/></svg>
      <span>1234567890</span>
    </div>
    <div class="web">
      <svg width="20" height="20" viewBox="0 0 24 24" aria-hidden="true"><g fill="none" stroke="#4bb8e0" stroke-width="1.8"><circle cx="12" cy="12" r="9"/><ellipse cx="12" cy="12" rx="4" ry="9"/><path d="M3 12h18M5 7h14M5 17h14"/></g></svg>
      <span>www.yourwebsite.com</span>
    </div>
  </div>
</div>
</body>
</html>
```